Finally a Vodka produced for women ! (Label Design)

We are a small distillery based in Melbourne, Australia and we need a Vodka label design solution that will appeal to women aged 30-50 years and radiate luxury. Full Details are in a design brief attached. We thank you in advance.

Target Market(s)

Affluent females 30-50 years.

Industry/Entity Type

Spirits/Alcohol

Requirements
Must have
• Be clear this is a luxury Vodka.
Nice to have
• Elegance.

```html
<!DOCTYPE html>
<html lang="en">
<head>
<meta charset="utf-8">
<title>Velvet Heron Premium Vodka – Label Dieline</title>
<link rel="stylesheet" href="https://fonts.googleapis.com/css2?family=Barlow:wght@400;500;600&family=Barlow+Condensed:wght@400;500&family=Barlow+Semi+Condensed:wght@400&display=swap">
<style>
  :root {
    --dieline: #00a0e3;
    --metallic-pink: #e4007c;
    --silver: #878787;
    --black: #111111;
    --varnish: #ececec;
    --pattern-grey: #dcdcdc;
    --paper: #ffffff;
  }
  html, body {
    margin: 0;
    padding: 0;
    width: 849px;
    height: 1200px;
    overflow: hidden;
    background: var(--paper);
  }
  .artboard { display: block; width: 849px; height: 1200px; }
  .guide { stroke: var(--dieline); stroke-width: 1.2; fill: none; }
  .guide-dashed { stroke: var(--dieline); stroke-width: 1; stroke-dasharray: 12 10; fill: none; }
  .arrowhead { fill: var(--dieline); }
  .dimension {
    font-family: "Barlow Semi Condensed", sans-serif;
    font-size: 25px;
    fill: var(--black);
  }
  .pattern-fill { fill: var(--pattern-grey); }
  .brand-name {
    font-family: "Barlow", sans-serif;
    font-weight: 600;
    fill: var(--metallic-pink);
    text-anchor: middle;
  }
  .tagline {
    font-family: "Barlow", sans-serif;
    font-weight: 400;
    text-anchor: middle;
  }
  .tagline--product { font-size: 18px; letter-spacing: 5px; fill: var(--black); }
  .tagline--filter { font-size: 24px; letter-spacing: 2.5px; fill: var(--silver); }
  .tagline--abv { font-size: 15px; letter-spacing: 5px; fill: var(--black); }
  .swatch-label {
    font-family: "Barlow Condensed", sans-serif;
    font-size: 15px;
    letter-spacing: 0.8px;
    fill: var(--black);
    text-anchor: middle;
  }
</style>
</head>
<body>
<svg class="artboard" viewBox="0 0 849 1200" xmlns="http://www.w3.org/2000/svg">
  <defs>
    <clipPath id="neck-band-clip">
      <rect x="218" y="130" width="397" height="198"/>
    </clipPath>
  </defs>

  <!-- Neck label -->
  <g class="neck-label">
    <text class="dimension" x="398" y="79" text-anchor="middle">100 mm</text>
    <line class="guide" x1="212" y1="88" x2="600" y2="88"/>
    <polygon class="arrowhead" points="208,88 220,82 216,88 220,94"/>
    <polygon class="arrowhead" points="604,88 592,82 596,88 592,94"/>

    <rect class="pattern-fill" x="218" y="130" width="397" height="198" role="img" aria-label="Soft grey repeating geometric background pattern"/>
    <g clip-path="url(#neck-band-clip)">
      <text class="brand-name" font-size="34"><tspan x="210" y="220">Velvet</tspan><tspan x="210" y="265">Heron</tspan></text>
      <text class="brand-name" font-size="34"><tspan x="390" y="220">Velvet</tspan><tspan x="390" y="265">Heron</tspan></text>
      <text class="brand-name" font-size="34"><tspan x="570" y="220">Velvet</tspan><tspan x="570" y="265">Heron</tspan></text>
    </g>
    <line class="guide-dashed" x1="218" y1="169" x2="615" y2="169"/>
    <line class="guide-dashed" x1="218" y1="288" x2="615" y2="288"/>
    <rect class="guide" x="218" y="130" width="397" height="198"/>

    <line class="guide" x1="674" y1="134" x2="674" y2="324"/>
    <polygon class="arrowhead" points="674,130 668,142 674,138 680,142"/>
    <polygon class="arrowhead" points="674,328 668,316 674,320 680,316"/>
    <text class="dimension" x="737" y="231" text-anchor="middle">50 mm</text>
  </g>

  <!-- Front label -->
  <g class="front-label">
    <text class="dimension" x="403" y="441" text-anchor="middle">108.57 mm</text>
    <line class="guide" x1="194" y1="465" x2="617" y2="465"/>
    <polygon class="arrowhead" points="190,465 202,459 198,465 202,471"/>
    <polygon class="arrowhead" points="621,465 609,459 613,465 609,471"/>
    <line class="guide" x1="190" y1="437" x2="190" y2="907"/>
    <line class="guide" x1="621" y1="437" x2="621" y2="907"/>

    <polygon class="pattern-fill" points="312,546 409,590 500,546 634,880 429,1013 382,1013 182,880" role="img" aria-label="Soft grey repeating geometric background pattern"/>

    <text class="brand-name" font-size="64"><tspan x="402" y="712">Velvet</tspan><tspan x="398" y="792">Heron</tspan></text>
    <text class="tagline tagline--product" x="405" y="843">PREMIUM VODKA</text>
    <text class="tagline tagline--filter" x="406" y="894">ROSE QUARTZ FILTERED</text>
    <text class="tagline tagline--abv" x="405" y="957">40% ALC/VOL</text>

    <polygon class="guide" points="318,558 409,596 494,558 621,878 429,1002 382,1002 190,878"/>

    <line class="guide" x1="521" y1="556" x2="741" y2="556"/>
    <line class="guide" x1="451" y1="1001" x2="741" y2="1001"/>
    <line class="guide" x1="699" y1="560" x2="699" y2="997"/>
    <polygon class="arrowhead" points="699,556 693,568 699,564 705,568"/>
    <polygon class="arrowhead" points="699,1001 693,989 699,993 705,989"/>
    <text class="dimension" x="761" y="793" text-anchor="middle">112.06 mm</text>
  </g>

  <!-- Print colour key -->
  <g class="colour-key">
    <rect x="57" y="1064" width="57" height="46" fill="var(--dieline)"/>
    <text class="swatch-label" x="86" y="1133">Guides/ dieline</text>
    <rect x="229" y="1064" width="57" height="46" fill="var(--metallic-pink)"/>
    <text class="swatch-label" x="254" y="1137">Metalic Pink</text>
    <rect x="364" y="1064" width="57" height="46" fill="var(--silver)"/>
    <text class="swatch-label" x="385" y="1139">Silver</text>
    <rect x="477" y="1064" width="57" height="46" fill="var(--black)"/>
    <text class="swatch-label" x="503" y="1137">Black</text>
    <rect x="620" y="1064" width="57" height="46" fill="var(--varnish)"/>
    <text class="swatch-label" x="647" y="1134">Gloss/Matt Varnish</text>
  </g>
</svg>
</body>
</html>
```